Design Large Inspirational Artwork with Long Quote

Design a large piece of art with a quote from Marcus Hallwell.

QUOTE
"The thing that's so interesting about being alive is that you're all in. No matter what you do, you're all in. This is gonna kill you, so I think you might as well play the most magnificent game you can while you're waiting. Because, do you have anything better to do? Why not pick the best thing possible that you could do? Because you're more powerful than you think, way more powerful than you think. I mean, God only knows what you are in the final analysis. You're blind to your own weaknesses, but you're also blind to your own strengths. How far could you take that if you stopped wasting time, and if you stopped lying, and if you oriented yourself to the highest possible good that you could conceive of and you committed to that? How much good could you do? Well, I would say: why don't you find out?"

SIZE
A high-resolution print size of 6' wide and 3' tall should provide ample space for both the quote and the accompanying artwork.

TYPOGRAPHY
Choose a bold, clean, and easily readable font for the quote. You could also experiment with different font sizes for certain words or phrases to emphasize their importance within the quote.

COLORS
Since the quote is thought-provoking and reflective, you might want to use a color palette that evokes a sense of introspection and depth. Consider using cool, calming colors like shades of blue, gray, or green. Alternatively, you can use a contrasting color scheme with a light background and dark text to make the quote stand out.

ARTWORK
Select / create / edit background artwork to complement the quote.
While a great design might be minimalistic and/or greyscale, I'd really like to see some full color options. This might be anything from photography or graphics inspired by the ideas in the text, to abstract colors or illustrations that feel like the sentiment expressed.
The art should capture your attention and encourage you to read the text. The art should be visually appealing, both at a distance and up close, regardless of whether the text is read.
Updates

Having trouble confirming the exact print size.

Still looking for printing solution and final size confirmation.

Target Market(s)

Personal, business, office

Industry/Entity Type

None

Font styles to use
Sans Serif
Script

Requirements
Must have
• Entire quote, legible text, modern design, attractive artwork, approx 6ft wide and 3ft tall
Nice to have
• Different font (sizes) for certain words or phrases to emphasize their importance within the quote.

```html
<!DOCTYPE html>
<html lang="en">
<head>
<meta charset="utf-8">
<title>Why Don't You Find Out? — Marcus Hallwell</title>
<link rel="stylesheet" href="https://fonts.googleapis.com/css2?family=Montserrat:wght@600;700;800&display=swap">
<style>
  :root {
    --sky-deep: #14162e;
    --sky-mid: #3b3f6b;
    --sky-light: #9a9cc4;
    --mist: #c9c9e0;
    --text: #ffffff;
    --tag-bg: #a9c6ff;
    --tag-text: #ffffff;
  }
  html, body {
    margin: 0;
    padding: 0;
    width: 1200px;
    height: 600px;
    overflow: hidden;
    background: var(--sky-deep);
  }
  .artwork {
    position: relative;
    width: 1200px;
    height: 600px;
    overflow: hidden;
    font-family: "Montserrat", sans-serif;
    color: var(--text);
  }
  .backdrop {
    position: absolute;
    inset: 0;
    background:
      radial-gradient(ellipse 55% 45% at 85% 30%, var(--mist) 0%, rgba(201,201,224,0) 70%),
      radial-gradient(ellipse 70% 50% at 80% 75%, rgba(90,94,140,0.9) 0%, rgba(59,63,107,0) 75%),
      linear-gradient(100deg, var(--sky-deep) 0%, #23264a 30%, var(--sky-mid) 60%, var(--sky-light) 100%);
  }
  .quote {
    position: absolute;
    inset: 0;
    margin: 0;
  }
  .line {
    position: absolute;
    white-space: nowrap;
    font-size: 12px;
    font-weight: 700;
    font-variant: small-caps;
    letter-spacing: 0.6px;
    line-height: 1;
  }
  .em {
    font-size: 20px;
    font-weight: 700;
    text-transform: uppercase;
    letter-spacing: 0.8px;
  }
  .em-big {
    font-size: 32px;
    font-weight: 800;
    text-transform: uppercase;
  }
  .finale {
    font-size: 31px;
    font-weight: 800;
    text-transform: uppercase;
    letter-spacing: 1.5px;
  }
  .author-tag {
    position: absolute;
    left: 744px;
    top: 524px;
    width: 216px;
    height: 36px;
    background: var(--tag-bg);
    color: var(--tag-text);
    font-family: "Montserrat", sans-serif;
    font-weight: 700;
    font-size: 21px;
    display: flex;
    align-items: center;
    justify-content: center;
  }
</style>
</head>
<body>
<main class="artwork">
  <div class="backdrop" role="img" aria-label="Twilight mountain landscape with a hiker standing on a rocky peak, looking out over misty ridges under a cloudy violet sky"></div>

  <blockquote class="quote">
    <p class="line" style="left:48px;top:50px">"The thing that's so <span class="em">interesting</span> about being <span class="em">alive</span> is that you're all in.</p>
    <p class="line" style="left:120px;top:72px">No <span class="em">matter</span> what you <span class="em">do</span>, you're all in.</p>
    <p class="line" style="left:336px;top:94px">this is gonna <span class="em">kill you</span>,</p>
    <p class="line" style="left:120px;top:124px">So I think you might as <span class="em">well play</span> the most <span class="em">magnificent game</span></p>
    <p class="line" style="left:448px;top:146px">you can while you're <span class="em">waiting</span>.</p>
    <p class="line" style="left:284px;top:168px">because, do you have anything <span class="em">better</span> to do?</p>
    <p class="line" style="left:198px;top:198px">Why not pick <span class="em">the best</span> thing <span class="em">possible</span> that you could do?</p>
    <p class="line" style="left:352px;top:222px">because you're more <span class="em">powerful</span> than you think,</p>
    <p class="line" style="left:484px;top:246px">way more <span class="em">powerful</span> than you think.</p>
    <p class="line" style="left:146px;top:270px">I mean, <span class="em-big">God</span> only knows what you are in <span class="em">the final analysis</span>.</p>
    <p class="line" style="left:400px;top:300px">you're <span class="em">blind</span> to your own <span class="em">weaknesses</span>,</p>
    <p class="line" style="left:368px;top:322px">but you're also <span class="em">blind</span> to your own <span class="em">strength</span></p>
    <p class="line" style="left:202px;top:352px">How far could you take that if you <span class="em">stopped wasting time</span>,</p>
    <p class="line" style="left:352px;top:376px">and if you <span class="em">stopped lying</span>,</p>
    <p class="line" style="left:418px;top:400px">and if you <span class="em">oriented yourself</span></p>
    <p class="line" style="left:448px;top:425px">to <span class="em">the highest possible good</span></p>
    <p class="line" style="left:160px;top:454px">that you could <span class="em">conceive</span> of and you <span class="em">committed</span> to that?</p>
    <p class="line" style="left:298px;top:480px">How much <span class="em">good</span> could you do?</p>
    <p class="line" style="left:400px;top:510px">well, I would say:</p>
    <p class="line finale" style="left:212px;top:528px">Why don't you find out?"</p>
  </blockquote>

  <div class="author-tag">Marcus Hallwell</div>
</main>
</body>
</html>
```